Bramble Peak Information Technology Business Card
Services for Move Add Change, Technical Relocation, Server Room Support, Technical Support
Bramble Peak Information Technology Business Card - Information Technology
Creative Brief
Professional
Owen Darlisk
2917 41st Lane Northeast Seattle WA 98422
owen@bramblepkit-example.com
www.bramblepkit-example.com
The original logo on the back, #34 and #35
Move Add and Changes, Corporate Relocation, Server Room Support, Technical Support

```html
<!DOCTYPE html>
<html lang="en">
<head>
<meta charset="utf-8">
<title>Bramble Peak Information Technology – Business Card</title>
<link href="https://fonts.googleapis.com/css2?family=Montserrat:wght@400;500;800&display=swap" rel="stylesheet">
<style>
  :root {
    --backdrop: #e9e7e4;
    --card-white: #ffffff;
    --panel-dark: #3b3b3d;
    --accent-orange: #f7941d;
    --logo-grey: #2f2f31;
    --text-light: #f2f2f2;
    --text-muted: #c9c9c9;
  }
  * { box-sizing: border-box; margin: 0; padding: 0; }
  html, body {
    width: 1200px; height: 901px; overflow: hidden;
    background: var(--backdrop);
    font-family: "Montserrat", Arial, sans-serif;
  }
  .stage {
    position: relative; width: 1200px; height: 901px;
    display: flex; flex-direction: column; align-items: center; justify-content: center; gap: 24px;
  }
  .card {
    position: relative; width: 680px; height: 389px;
    background: var(--card-white);
    border-radius: 26px; overflow: hidden;
    box-shadow: 0 6px 22px rgba(0,0,0,.16);
  }
  .card-shape { position: absolute; inset: 0; }
  .wordmark {
    position: absolute;
    font-weight: 800; color: var(--logo-grey);
    letter-spacing: 0.5px; text-transform: uppercase; line-height: 1;
    white-space: nowrap;
    display: flex; align-items: center; gap: 8px;
  }
  .wordmark .dot {
    width: 12px; height: 12px; border-radius: 50%; background: var(--accent-orange); flex: none;
  }
  .front .wordmark { left: 36px; top: 172px; font-size: 22px; }
  .back .wordmark { left: 50%; top: 50%; transform: translate(-50%, -50%); font-size: 38px; gap: 12px; }
  .back .wordmark .dot { width: 16px; height: 16px; }
  .contact {
    position: absolute; left: 420px; top: 74px; width: 225px;
    color: var(--text-light);
  }
  .contact .name { font-size: 17px; font-weight: 500; letter-spacing: 1px; text-transform: uppercase; white-space: nowrap; }
  .contact .role { font-size: 12px; color: var(--text-muted); margin-top: 4px; }
  .contact .address { font-size: 12px; line-height: 1.6; margin-top: 52px; }
  .lines { list-style: none; margin-top: 44px; }
  .lines li {
    display: flex; justify-content: space-between; align-items: center; gap: 6px;
    font-size: 12px; height: 23px; white-space: nowrap;
  }
  .lines li.web { font-size: 10.5px; }
  .lines svg { width: 13px; height: 13px; flex: none; fill: var(--text-light); }
</style>
</head>
<body>
<main class="stage">

  <section class="card front" aria-label="Business card front">
    <svg class="card-shape" viewBox="0 0 680 389" aria-hidden="true">
      <path d="M372 0 C 285 110, 292 270, 350 389 L360 389 C 305 270, 300 115, 392 0 Z" fill="var(--accent-orange)"/>
      <path d="M392 0 C 300 115, 305 270, 360 389 L680 389 L680 0 Z" fill="var(--panel-dark)"/>
    </svg>

    <div class="wordmark"><span class="dot"></span>Bramble Peak</div>

    <div class="contact">
      <p class="name">Owen Darlisk</p>
      <p class="role">Managing Director</p>
      <p class="address">2917 41st Lane Northeast<br>Seattle WA 98422</p>
      <ul class="lines">
        <li>206 555 0147
          <svg viewBox="0 0 24 24"><path d="M6.6 10.8a15 15 0 0 0 6.6 6.6l2.2-2.2c.3-.3.7-.4 1-.2 1.1.4 2.3.6 3.6.6.6 0 1 .4 1 1V20c0 .6-.4 1-1 1A17 17 0 0 1 3 4c0-.6.4-1 1-1h3.5c.6 0 1 .4 1 1 0 1.3.2 2.5.6 3.6.1.3 0 .7-.2 1z"/></svg>
        </li>
        <li>206 555 0148
          <svg viewBox="0 0 24 24"><path d="M7 2h10a1 1 0 0 1 1 1v18a1 1 0 0 1-1 1H7a1 1 0 0 1-1-1V3a1 1 0 0 1 1-1zm1 3v12h8V5zm4 13.5a1 1 0 1 0 0 2 1 1 0 0 0 0-2z"/></svg>
        </li>
        <li>206 555 0149
          <svg viewBox="0 0 24 24"><path d="M6 2h9l4 4v5H6zm-2 10h16a1 1 0 0 1 1 1v8H3v-8a1 1 0 0 1 1-1zm3 3v2h10v-2z"/></svg>
        </li>
        <li>owen@bramblepkit-example.com
          <svg viewBox="0 0 24 24"><path d="M3 5h18v14H3zm2 2v.5l7 5 7-5V7zm0 3v7h14v-7l-7 5z"/></svg>
        </li>
        <li class="web">www.bramblepkit-example.com
          <svg viewBox="0 0 24 24"><path d="M12 2a10 10 0 1 0 0 20 10 10 0 0 0 0-20zm0 2c.9 1.2 1.6 2.9 1.9 5h-3.8c.3-2.1 1-3.8 1.9-5zM4.3 11h3.8c0 1.4.1 2.8.4 4H5a8 8 0 0 1-.7-4zm5.8 0h3.8c0 1.5-.1 2.8-.4 4h-3c-.3-1.2-.4-2.5-.4-4zm5.8 0h3.8a8 8 0 0 1-.7 4h-3.5c.3-1.2.4-2.6.4-4zM12 20c-.7-.8-1.2-2-1.6-3h3.2c-.4 1-.9 2.2-1.6 3z"/></svg>
        </li>
      </ul>
    </div>
  </section>

  <section class="card back" aria-label="Business card back">
    <div class="wordmark"><span class="dot"></span>Bramble Peak</div>
  </section>

</main>
</body>
</html>
```